Maple Hollow Canine Massage Needs a Business Card Design

Maple Hollow Canine Massage is a new therapeutic canine massage company located in Nederland, Colorado. I need a business card design that include my logo and basic contact information.

Target Market(s)

Pet owners, veterinarians

Industry/Entity Type

Business

Contact Information for Business Card

Lydia Ferrow, CCMT
303.518.7269
lydia@maplehollowmassage.example
www.maplehollowmassage.example

Colors
6c459b
886aae
b8a6cd
a64599
b768aa
d3a5cc
fbed22

Requirements
Must have
• Font should be similar to font in logo.

```html
<!DOCTYPE html>
<html lang="en">
<head>
<meta charset="utf-8">
<title>Maple Hollow Canine Massage – Business Card</title>
<link href="https://fonts.googleapis.com/css2?family=Nunito:wght@600;700;800&display=swap" rel="stylesheet">
<style>
  :root {
    --page-bg: #ece8f0;
    --card-bg: #ffffff;
    --band: #b384bd;
    --gold: #f1d54a;
    --badge: #6c459b;
    --name: #b768aa;
    --ink: #4a2f66;
    --web: #a964b0;
    --mark-tint: #d9d2e6;
  }
  * { box-sizing: border-box; margin: 0; padding: 0; }
  html, body {
    width: 1200px;
    height: 902px;
    overflow: hidden;
    background: var(--page-bg);
    font-family: "Nunito", "Helvetica Neue", Arial, sans-serif;
  }
  .business-card {
    position: absolute;
    left: 50px;
    top: 138px;
    width: 1100px;
    height: 626px;
    background: var(--card-bg);
    overflow: hidden;
    box-shadow: 0 6px 24px rgba(60, 40, 80, 0.18);
  }
  .side-band {
    position: absolute;
    left: 0; top: 0;
    width: 152px; height: 100%;
    background: var(--band);
  }
  .gold-rule {
    position: absolute;
    left: 156px; top: 0;
    width: 6px; height: 100%;
    background: var(--gold);
  }
  .brand-badge {
    position: absolute;
    left: 47px; top: 44px;
    width: 256px; height: 256px;
    border-radius: 50%;
    background: var(--card-bg);
    border: 4px solid var(--gold);
    display: flex;
    align-items: center;
    justify-content: center;
  }
  .brand-badge-disc {
    width: 226px; height: 226px;
    border-radius: 50%;
    background: var(--badge);
    display: flex;
    align-items: center;
    justify-content: center;
    text-align: center;
    padding: 0 24px;
  }
  .brand-name {
    color: var(--gold);
    font-weight: 800;
    font-size: 25px;
    line-height: 1.15;
    text-transform: uppercase;
  }
  .decor-mark {
    position: absolute;
    left: 700px; top: 70px;
    width: 420px; height: 520px;
    background: radial-gradient(ellipse at 45% 50%, var(--mark-tint) 0%, rgba(217,210,230,0.55) 45%, rgba(255,255,255,0) 72%);
  }
  .holder-name {
    position: absolute;
    left: 289px; top: 322px;
    color: var(--name);
    font-weight: 800;
    font-size: 41px;
    letter-spacing: 0.3px;
  }
  .contact-list {
    position: absolute;
    left: 289px; top: 440px;
    list-style: none;
  }
  .contact-item {
    display: flex;
    align-items: center;
    height: 40px;
    color: var(--ink);
    font-weight: 600;
    font-size: 31px;
  }
  .contact-icon {
    width: 28px; height: 28px;
    background: var(--gold);
    margin-right: 12px;
    display: flex;
    align-items: center;
    justify-content: center;
    flex-shrink: 0;
  }
  .website {
    position: absolute;
    left: 292px; top: 532px;
    color: var(--web);
    font-weight: 800;
    font-size: 28px;
    letter-spacing: 1.6px;
  }
</style>
</head>
<body>
  <main class="business-card">
    <div class="side-band"></div>
    <div class="gold-rule"></div>

    <div class="decor-mark" role="img" aria-label="Faint large brand decoration area"></div>

    <div class="brand-badge">
      <div class="brand-badge-disc">
        <span class="brand-name">Maple Hollow Canine Massage</span>
      </div>
    </div>

    <h1 class="holder-name">Lydia Ferrow, CCMT</h1>

    <ul class="contact-list">
      <li class="contact-item">
        <span class="contact-icon">
          <svg width="18" height="18" viewBox="0 0 24 24" aria-hidden="true">
            <path d="M6.6 10.8c1.4 2.8 3.8 5.1 6.6 6.6l2.2-2.2c.3-.3.7-.4 1-.2 1.1.4 2.3.6 3.6.6.6 0 1 .4 1 1V20c0 .6-.4 1-1 1C10.6 21 3 13.4 3 4c0-.6.4-1 1-1h3.5c.6 0 1 .4 1 1 0 1.3.2 2.5.6 3.6.1.3 0 .7-.2 1L6.6 10.8z" fill="#a964b0"/>
          </svg>
        </span>
        303.518.7269
      </li>
      <li class="contact-item">
        <span class="contact-icon">
          <svg width="18" height="14" viewBox="0 0 20 14" aria-hidden="true">
            <rect x="0.5" y="0.5" width="19" height="13" fill="#a964b0"/>
            <path d="M0.5 0.5 L10 8 L19.5 0.5" fill="none" stroke="#f1d54a" stroke-width="1.4"/>
          </svg>
        </span>
        lydia@maplehollowmassage.example
      </li>
    </ul>

    <p class="website">www.maplehollowmassage.example</p>
  </main>
</body>
</html>
```